Natural Immune System Booster

We need a pharmaceutical type box and label design for a vitamin supplement product. Pravolex is in process of being trademarked and should therefore carry the TM symbol. It is comprised of a special blend of over 20 vitamins, herbs and minerals with a High strength vitamin C booster. The tag line should read. The No.1 Natural Support For Your Immune System. Each tube contains 10 tablets. A bar code will be placed on the box carton. We prefer bright and vivid colours, preferably a mix of electric purple, yellow and orange mix. We have three flavours, summer berry (strawberry), tropical fruit and juicy orange - the box and label should indicate the flavours in a creative design element. Effervescent tabelts should be clearly marked on the box and label. The ingredients and instructions should be present on the box outer carton and also the label. We require an eye catching yet simple and bright design that pops off the shelf.
Updates

Target Market(s)

Target customers are male and female 20 - 60+ that live in Western countries that handle household budgets.

Industry/Entity Type

Pharmaceutical

Requirements
Must have
• Please see current box design, all necessary elements and specifications are included here. We require same to be placed on new design.

I have attached a txt file of the supplement facts and other details that are required for both the label and the box

```html
<!DOCTYPE html>
<html lang="en">
<head>
<meta charset="utf-8">
<title>Pravolex – Label and Carton Panels</title>
<link rel="stylesheet" href="https://fonts.googleapis.com/css2?family=Jost:wght@700&family=Oswald:wght@400&display=swap">
<style>
  :root {
    --purple-deep: #7a2a8e;
    --purple-mid: #9a5aae;
    --purple-pale: #f1e6f4;
    --yellow: #fff200;
    --orange: #f7821e;
    --white: #ffffff;
    --bubble-a: rgba(190, 205, 240, 0.75);
    --bubble-b: rgba(150, 160, 220, 0.0);
  }
  * { margin: 0; padding: 0; box-sizing: border-box; }
  html, body { width: 1164px; height: 1200px; overflow: hidden; background: var(--white); }
  .canvas { position: relative; width: 1164px; height: 1200px; }

  .panel { position: absolute; overflow: hidden; box-shadow: 4px 5px 6px rgba(0,0,0,0.35); }

  /* Square label */
  .label-square {
    left: 166px; top: 155px; width: 378px; height: 423px;
    background: linear-gradient(90deg, var(--purple-pale) 0%, var(--purple-mid) 18%, var(--purple-deep) 45%, var(--purple-deep) 60%, var(--purple-mid) 82%, var(--purple-pale) 100%);
  }
  .label-square .flavour {
    position: absolute; left: 0; width: 388px; top: 18px; text-align: center;
    font-family: "Oswald", sans-serif; font-size: 17px; color: var(--white); letter-spacing: 0.2px;
  }
  .label-square .brand {
    position: absolute; left: 142px; top: 45px; height: 350px; width: 60px;
    writing-mode: vertical-rl; transform: rotate(180deg);
    font-family: "Jost", sans-serif; font-weight: 700; font-size: 72px; line-height: 60px;
    color: var(--yellow); white-space: nowrap;
  }
  .label-square .tm {
    position: absolute; left: 180px; top: 47px; writing-mode: vertical-rl; transform: rotate(180deg);
    font-family: "Jost", sans-serif; font-weight: 700; font-size: 8px; color: var(--yellow);
  }
  .label-square .tagline-band {
    position: absolute; left: 212px; top: 60px; width: 22px; height: 363px;
    background: var(--orange); border-right: 4px solid var(--white);
    writing-mode: vertical-rl; transform: rotate(180deg);
    font-family: "Oswald", sans-serif; font-size: 13.5px; line-height: 18px; color: var(--white);
    white-space: nowrap; padding-top: 30px;
  }
  .label-square .bubbles {
    position: absolute; left: 20px; top: 245px; width: 358px; height: 178px;
    background: radial-gradient(ellipse at 92% 70%, var(--bubble-a) 0%, rgba(170,180,230,0.45) 40%, var(--bubble-b) 75%);
  }

  /* Wide carton front */
  .carton-front {
    left: 156px; top: 696px; width: 880px; height: 320px;
    background: linear-gradient(180deg, var(--purple-pale) 0%, var(--purple-mid) 18%, var(--purple-deep) 40%, var(--purple-deep) 62%, var(--purple-mid) 84%, var(--purple-pale) 100%);
  }
  .carton-front .brand {
    position: absolute; left: 50px; top: 24px;
    font-family: "Jost", sans-serif; font-weight: 700; font-size: 125px; line-height: 1;
    color: var(--yellow); white-space: nowrap;
  }
  .carton-front .tm {
    position: absolute; left: 634px; top: 131px;
    font-family: "Jost", sans-serif; font-weight: 700; font-size: 10px; color: var(--yellow);
  }
  .carton-front .tagline-band {
    position: absolute; left: 0; top: 164px; width: 632px; height: 46px;
    background: var(--orange); border-bottom: 5px solid var(--white);
    font-family: "Oswald", sans-serif; font-size: 25px; line-height: 41px; color: var(--white);
    padding-left: 54px; white-space: nowrap;
  }
  .carton-front .flavour {
    position: absolute; left: 58px; top: 224px;
    font-family: "Oswald", sans-serif; font-size: 29px; letter-spacing: 1.2px; color: var(--white); white-space: nowrap;
  }
  .carton-front .bubbles {
    position: absolute; left: 520px; top: 125px; width: 360px; height: 195px;
    background: radial-gradient(ellipse at 85% 75%, var(--bubble-a) 0%, rgba(170,180,230,0.45) 40%, var(--bubble-b) 75%);
  }
</style>
</head>
<body>
<div class="canvas">
  <section class="panel label-square">
    <div class="bubbles" role="img" aria-label="Cluster of effervescent bubbles"></div>
    <p class="flavour">JUICY ORANGE</p>
    <h1 class="brand">Pravolex</h1>
    <span class="tm">TM</span>
    <p class="tagline-band">THE NO.1 NATURAL SUPPORT FOR YOUR IMMUNE SYSTEM</p>
  </section>

  <section class="panel carton-front">
    <div class="bubbles" role="img" aria-label="Cluster of effervescent bubbles"></div>
    <h2 class="brand">Pravolex</h2>
    <span class="tm">TM</span>
    <p class="tagline-band">THE NO.1 NATURAL SUPPORT FOR YOUR IMMUNE SYSTEM</p>
    <p class="flavour">JUICY ORANGE EFFERVESCENT TABLETS</p>
  </section>
</div>
</body>
</html>
```